Business Card Design

I am a realtor and i also flip houses. I am CEO and Founder of my business which is Halvorsen Group LLC which is named after my great uncle who died and i was really close to. He was a wonderful friendly man so i want my business to represent him too. My business works with a lot of different people but i want mainly something to show i am a strong confidant woman who owns there own business. I have a really fun personality so i don't want anything TOO serious or manly. I want the perfect mix. My last two business cards i created are too embarrassing to hand out because they are far too girly and i deal with a lot of millionaire clients. I live out in the Palm Springs California area. I think its very important to show i am a single mom, female with her own business at only 24. I don't want to just be a female that blends in with all of the other serious people but yet i don't want to seem immature. People are telling me to stay away from pinks and purples but i don't want blues and greens because they represent men more. But i won't say no to them if there is a happy medium.

Industry/Entity Type

Realtor

Contact Information for Business Card

Halvorsen Group, LLC
Corinne Pell
27318 Quillan Ave, B1 582
Rancho Mirage, CA 92270
760-555-0147
Corinnetpell@mailverta.com

```html
<!DOCTYPE html>
<html lang="en">
<head>
<meta charset="utf-8">
<title>Halvorsen Group LLC – Business Card</title>
<link href="https://fonts.googleapis.com/css2?family=Source+Sans+3:wght@400;600&display=swap" rel="stylesheet">
<style>
  :root {
    --backdrop: #6b6b6b;
    --card: #ebe9e6;
    --band: #e0d8ce;
    --ink: #2b2b2b;
    --ink-soft: #3a3a3a;
    --accent: #b98a5e;
  }
  * { margin: 0; padding: 0; box-sizing: border-box; }
  html, body {
    width: 1200px; height: 1200px; overflow: hidden;
    background: var(--backdrop);
    font-family: "Source Sans 3", "Helvetica Neue", Arial, sans-serif;
    color: var(--ink);
  }
  .sheet { position: relative; width: 1200px; height: 1200px; }
  .card {
    position: absolute; left: 180px;
    width: 840px; height: 480px;
    background: linear-gradient(to bottom,
      var(--band) 0, var(--band) 13%,
      var(--card) 13%, var(--card) 87%,
      var(--band) 87%, var(--band) 100%);
    box-shadow: 0 10px 24px rgba(0,0,0,.28);
  }
  .card--back { top: 90px; }
  .card--front { top: 630px; }

  .brand {
    position: absolute;
    font-weight: 600; font-size: 34px; letter-spacing: .2px;
    color: var(--ink); white-space: nowrap;
  }
  .card--back .brand { left: 50%; top: 50%; transform: translate(-50%, -50%); }
  .card--front .brand { left: 56px; top: 196px; font-size: 31px; }

  .divider-strokes { position: absolute; left: 392px; top: 180px; }

  .holder {
    position: absolute; right: 70px; top: 92px; width: 260px;
    border-bottom: 2px solid var(--accent);
  }
  .holder__name {
    font-size: 30px; font-variant: small-caps; letter-spacing: 1px;
    line-height: 1; color: var(--ink);
  }
  .holder__title {
    font-size: 13px; letter-spacing: 1px; text-transform: uppercase;
    padding: 2px 0 4px; color: var(--accent);
  }

  .contact {
    position: absolute; left: 402px; top: 312px;
    list-style: none; font-size: 16px; line-height: 26px; color: var(--ink-soft);
    white-space: nowrap;
  }
  .contact__label { display: inline-block; width: 24px; color: var(--accent); font-weight: 600; }
</style>
</head>
<body>
<main class="sheet">
  <section class="card card--back" aria-label="Card back">
    <div class="brand">Halvorsen Group LLC</div>
  </section>

  <section class="card card--front" aria-label="Card front">
    <div class="brand">Halvorsen Group LLC</div>

    <svg class="divider-strokes" width="36" height="116" viewBox="0 0 36 116" aria-hidden="true">
      <g stroke="#b98a5e" stroke-width="1.6">
        <line x1="18" y1="18" x2="2" y2="92"/>
        <line x1="26" y1="8" x2="8" y2="104"/>
        <line x1="34" y1="0" x2="14" y2="116"/>
      </g>
    </svg>

    <div class="holder">
      <div class="holder__name">Corinne Pell</div>
      <div class="holder__title">Owner</div>
    </div>

    <ul class="contact">
      <li><span class="contact__label">E:</span>Corinnetpell@mailverta.com</li>
      <li><span class="contact__label">P:</span>760-555-0147</li>
      <li><span class="contact__label">A:</span>27318 Quillan Ave, B1 582 Rancho Mirage, CA 92270</li>
    </ul>
  </section>
</main>
</body>
</html>
```